Tove & Lark Designs - Promotions flyer

I am a locally based Interior designer /stylist on Sydney's lower north shore. I would like to offer my services:
Full Professional Styling Services and Furniture Hire
Colour Consultation – Interior / exterior
Floor Coverings
Furniture selection and sourcing
Window Treatments
Wallpaper
Soft Furnishings
Upholstery
Renovations

I would like to offer a free consultation
Updates

Project Deadline Extended
Reason: I've been speaking with a designer and need her to make one more change. I have tried to message her twice, but have had no reply. Once she makes these changes I'm ready to sign off on the design. Thanks Harriet

Target Market(s)

30 - 60's middle to high income earners

Industry/Entity Type

Floor

Requirements
Must have
• one sided DL size
Use my logo
1 or 2 images of interior space or image of a lamp, cushion, lounge etc
The following contact details:
Mobile: 041 xxx xxxx
Website Address: www.tovelarkdesigns.example.au

```html
<!DOCTYPE html>
<html lang="en">
<head>
<meta charset="utf-8">
<title>Tove &amp; Lark Designs – DL Flyer</title>
<link rel="stylesheet" href="https://fonts.googleapis.com/css2?family=Oswald:wght@500;700&family=Roboto+Condensed:wght@400;700&display=swap">
<style>
  :root {
    --stage: #1b1b1b;
    --paper: #ffffff;
    --orange: #f26a1b;
    --grey: #6d6e70;
    --grey-dark: #4a4b4d;
    --ink: #58595b;
    --wall: #d4d6da;
    --wall-shade: #aeb1b7;
    --linen: #eceef1;
    --cushion: #8d9099;
    --throw: #5f6472;
    --floor: #3a3d44;
  }
  * { box-sizing: border-box; margin: 0; padding: 0; }
  html, body {
    width: 1200px; height: 755px; overflow: hidden;
    background: var(--stage);
  }
  .flyer {
    position: absolute; left: 430px; top: 20px;
    width: 340px; height: 715px;
    background: var(--paper); overflow: hidden;
    font-family: "Roboto Condensed", "Arial Narrow", sans-serif;
  }
  .brand {
    position: absolute; top: 30px; left: 0; width: 100%;
    display: flex; justify-content: center; align-items: center; gap: 10px;
    color: var(--orange); font-size: 31px; font-weight: 400;
  }
  .brand-dot {
    width: 22px; height: 22px; border-radius: 50%; background: var(--grey-dark);
  }
  .web-band {
    position: absolute; top: 92px; left: 0; width: 100%; height: 26px;
    background: var(--orange); color: var(--paper);
    font-weight: 700; font-size: 14px; line-height: 26px;
    text-align: center; letter-spacing: 0.3px;
  }
  .headline {
    position: absolute; top: 136px; left: 24px; width: 300px;
    font-family: "Oswald", "Arial Narrow", sans-serif; font-weight: 700;
    text-transform: uppercase; line-height: 1; color: var(--ink);
    transform: rotate(-6deg); transform-origin: left top;
  }
  .headline span { display: block; }
  .headline .l1 { font-size: 25px; }
  .headline .l2 { font-size: 36px; }
  .headline .l3 { font-size: 24px; }
  .headline em { font-style: normal; color: var(--orange); }
  .photo {
    position: absolute; top: 270px; left: 0; width: 100%; height: 445px;
    clip-path: polygon(0 22%, 100% 0, 100% 100%, 0 100%);
    background: linear-gradient(172deg,
      var(--wall) 0%, var(--wall-shade) 28%, var(--linen) 46%,
      var(--cushion) 62%, var(--throw) 78%, var(--floor) 100%);
  }
  .photo-inset {
    position: absolute; top: 345px; left: 192px; width: 130px; height: 100px;
    border: 5px solid var(--paper);
    background: linear-gradient(135deg, #f1f2f6 0%, #b9bbd0 45%, #3b3564 100%);
    transform: rotate(8deg);
    box-shadow: 0 4px 10px rgba(0,0,0,.35);
  }
  .services {
    position: absolute; top: 250px; left: 0; list-style: none;
  }
  .services li {
    height: 23px; margin-bottom: 6px; padding: 0 12px 0 12px;
    width: fit-content; color: var(--paper);
    font-size: 14px; line-height: 23px; text-transform: uppercase;
  }
  .services .grey { background: var(--grey); }
  .services .orange { background: var(--orange); font-weight: 700; }
  .services .two-line { height: 36px; line-height: 16px; padding-top: 2px; }
  .phone-band {
    position: absolute; top: 630px; left: 0; width: 100%; height: 46px;
    background: rgba(74,75,77,.9); color: var(--paper);
    display: flex; align-items: center; gap: 12px; padding-left: 20px;
    font-family: "Oswald", "Arial Narrow", sans-serif; font-weight: 500;
    font-size: 32px; letter-spacing: 1px;
  }
  .call-tab {
    position: absolute; top: 676px; right: 0; height: 24px; padding: 0 14px;
    background: var(--orange); color: var(--paper);
    font-weight: 700; font-size: 13.5px; line-height: 24px;
  }
</style>
</head>
<body>
  <main class="flyer">
    <div class="brand"><span>Tove &amp; Lark Designs</span><span class="brand-dot"></span></div>
    <div class="web-band">WWW.TOVELARKDESIGNS.EXAMPLE.AU</div>

    <h1 class="headline">
      <span class="l1">Full Professional</span>
      <span class="l2"><em>Styling</em> Services</span>
      <span class="l3">And <em>Furniture</em> Hire</span>
    </h1>

    <div class="photo" role="img" aria-label="Photo of a styled bedroom with a carved headboard, silver cushions, white linen and a lamp"></div>
    <div class="photo-inset" role="img" aria-label="Close-up photo of a purple cushion on a white chair"></div>

    <ul class="services">
      <li class="grey two-line">Colour consultation –<br>interior / exterior</li>
      <li class="orange">Floor coverings</li>
      <li class="grey">Furniture selection and sourcing</li>
      <li class="orange">Window treatments</li>
      <li class="grey">Wallpaper</li>
      <li class="orange">Soft furnishings</li>
      <li class="grey">Upholstery</li>
      <li class="orange">Renovations</li>
    </ul>

    <div class="phone-band">
      <svg width="30" height="30" viewBox="0 0 30 30" aria-hidden="true">
        <circle cx="15" cy="15" r="13" fill="none" stroke="#fff" stroke-width="2"/>
        <path d="M10 8c1-1 2-1 3 0l1.5 2.5c.5 1 0 1.8-.7 2.3l-.8.6c.6 1.7 2 3.2 3.6 3.9l.6-.8c.6-.7 1.4-1.1 2.3-.6L22 17.4c1 .9 1 2 0 3-2 2-5 1.5-8-1.5S8 10 10 8z" fill="#fff"/>
      </svg>
      <span>041 XXX XXXX</span>
    </div>
    <div class="call-tab">CALL US TODAY!</div>
  </main>
</body>
</html>
```